Easy one-page Web Design with ready made sketch/template

This project have an already made one page Web Design sketch/template that should be used as a base. It needs professional touch and improvements but should be quite straight forward for you to make.

Webpage: Offers local graphical design services

Attached following documents for you:
- PSD sketch
- JPG sketch
- Word file with project description (read carefully)
- Logo

Reason: Project extended to get the final designs submitted. Thanks

Target Market(s)

Logo design

Industry/Entity Type

Graphic Design

Number of Pages Required

1 page

Requirements
Must have
• Please refer to attached word document.
Nice to have
Should not have

```html
<!DOCTYPE html>
<html lang="sv">
<head>
<meta charset="utf-8">
<title>Markverket – Ny Logotyp</title>
<link rel="stylesheet" href="https://fonts.googleapis.com/css2?family=Montserrat:wght@400;600;700&family=Nunito+Sans:wght@300;400;600&display=swap">
<style>
  :root {
    --brand-blue: #2ba8e0;
    --ink: #111111;
    --muted: #b9b9b9;
    --orange: #fb9a3a;
    --orange-deep: #ee8422;
    --yellow: #fbb84e;
    --green: #3a8f35;
    --green-deep: #2f7f2a;
    --red: #e2323a;
    --white: #ffffff;
    --hero-light: #f2f2f2;
    --hero-mid: #c9c9c9;
  }
  * { box-sizing: border-box; margin: 0; padding: 0; }
  html, body { width: 1200px; height: 900px; overflow: hidden; background: var(--white); }
  body { position: relative; font-family: "Nunito Sans", Arial, sans-serif; color: var(--ink); }

  .site-header { position: absolute; left: 0; top: 0; width: 1200px; height: 139px; background: var(--white); z-index: 2; }
  .brand { position: absolute; left: 45px; top: 50px; display: flex; align-items: center; gap: 10px;
    font-family: "Montserrat", sans-serif; font-weight: 600; font-size: 30px; color: var(--brand-blue); letter-spacing: 0.5px; }
  .brand-square { width: 16px; height: 16px; background: var(--brand-blue); }
  .main-nav { position: absolute; top: 61px; left: 283px; display: flex; font-family: "Montserrat", sans-serif; font-weight: 700; font-size: 16px; letter-spacing: 0.4px; }
  .main-nav a { color: var(--ink); text-decoration: none; position: absolute; white-space: nowrap; }
  .order-button { position: absolute; left: 699px; top: 46px; width: 208px; height: 52px; border-radius: 26px; background: var(--orange);
    display: flex; align-items: center; padding-left: 16px; gap: 20px; color: var(--white);
    font-family: "Montserrat", sans-serif; font-weight: 700; font-size: 16px; letter-spacing: 0.4px; }
  .order-button .icon { width: 30px; height: 30px; border-radius: 50%; background: var(--white); display: flex; align-items: center; justify-content: center; }
  .call { position: absolute; left: 959px; top: 52px; }
  .call-label { font-family: "Montserrat", sans-serif; font-weight: 600; font-size: 10px; letter-spacing: 9px; }
  .call-number { font-family: "Nunito Sans", sans-serif; font-weight: 300; font-size: 27px; line-height: 1; letter-spacing: 0.5px; }

  .hero { position: absolute; left: 0; top: 139px; width: 1200px; height: 666px; }
  .hero-photo { position: absolute; inset: 0;
    background: radial-gradient(ellipse 45% 45% at 50% 50%, var(--hero-light) 0%, #e6e6e6 60%, var(--hero-mid) 100%); }
  .hero-content { position: absolute; left: 0; top: 0; width: 1200px; text-align: center; }
  .hero-title { position: absolute; left: 0; width: 1200px; top: 158px; font-weight: 400; font-size: 45px; letter-spacing: 1px; }
  .hero-lead { position: absolute; left: 270px; width: 660px; top: 232px; font-size: 19px; line-height: 28px; color: var(--muted); }
  .how-button { position: absolute; left: 486px; top: 327px; width: 225px; height: 51px; border: 2px solid var(--brand-blue); border-radius: 26px;
    display: flex; align-items: center; padding-left: 18px; gap: 22px; font-family: "Montserrat", sans-serif; font-weight: 700; font-size: 11px; letter-spacing: 1px; color: #333; }
  .how-button .play { width: 26px; height: 26px; border-radius: 50%; background: var(--brand-blue); display: flex; align-items: center; justify-content: center; }
  .price-line { position: absolute; left: 0; width: 1200px; top: 448px; font-size: 27px; color: #555; }
  .price-line strong { color: var(--red); font-weight: 600; }
  .scroll-cue { position: absolute; left: 592px; top: 515px; }

  .tile { position: absolute; color: var(--white); text-align: center; }
  .tile-guarantee { left: 62px; top: 723px; width: 323px; height: 177px; background: var(--yellow); color: var(--ink); }
  .tile-order { left: 385px; top: 695px; width: 437px; height: 205px; background: linear-gradient(135deg, var(--orange) 0%, var(--orange-deep) 100%); }
  .tile-reviews { left: 822px; top: 720px; width: 345px; height: 180px; background: linear-gradient(160deg, var(--green-deep) 0%, var(--green) 100%); }
  .tile-guarantee .trophy { position: absolute; left: 137px; top: 30px; }
  .tile-guarantee .label { position: absolute; left: 0; width: 323px; top: 92px; font-size: 21px; letter-spacing: 1px; }
  .tile-guarantee .value { position: absolute; left: 0; width: 323px; top: 120px; font-size: 30px; letter-spacing: 1px; }
  .tile-order .title { position: absolute; left: 0; width: 437px; top: 22px; font-size: 25px; letter-spacing: 1px; }
  .tile-order .clock { position: absolute; left: 174px; top: 60px; }
  .tile-order .price { position: absolute; left: 0; width: 437px; top: 168px; font-size: 24px; letter-spacing: 1px; }
  .tile-reviews .stars { position: absolute; left: 85px; top: 22px; }
  .tile-reviews .score { position: absolute; left: 0; width: 345px; top: 68px; font-size: 21px; letter-spacing: 0.6px; }
  .tile-reviews .count { position: absolute; left: 0; width: 345px; top: 99px; font-size: 17px; letter-spacing: 0.6px; }
  .tile-reviews .love { position: absolute; left: 0; width: 345px; top: 113px; font-size: 24px; letter-spacing: 0.6px; }
  .tile-reviews .source { position: absolute; left: 0; width: 345px; top: 142px; font-size: 17px; display: flex; justify-content: center; align-items: center; gap: 4px; color: #1b1b1b; }
</style>
</head>
<body>
  <header class="site-header">
    <div class="brand"><span class="brand-square"></span>Markverket</div>
    <nav class="main-nav">
      <a style="left:0">PRODUCT</a>
      <a style="left:135px">GALLERY</a>
      <a style="left:255px">CONTACT US</a>
    </nav>
    <div class="order-button">
      <span class="icon"><svg width="14" height="10" viewBox="0 0 14 10"><path d="M2 2 L7 7 L12 2" fill="none" stroke="#fb9a3a" stroke-width="3" stroke-linecap="round"/></svg></span>
      ORDER LOGO
    </div>
    <div class="call">
      <div class="call-label">RING</div>
      <div class="call-number">08-12 34 5678</div>
    </div>
  </header>

  <section class="hero">
    <div class="hero-photo" role="img" aria-label="Designer's desk seen from above with a lamp, paint pots and pencils in soft grey tones"></div>
    <div class="hero-content">
      <h1 class="hero-title">Ny Logotyp / Företagslogga?</h1>
      <p class="hero-lead">We tailor your professional company logo and send you the first drafts already within 24 hours</p>
      <div class="how-button">
        <span class="play"><svg width="10" height="12" viewBox="0 0 10 12"><path d="M1 0 L10 6 L1 12 Z" fill="#fff"/></svg></span>
        HOW IT WORKS?
      </div>
      <p class="price-line">Start From <strong>$1495</strong></p>
      <svg class="scroll-cue" width="16" height="10" viewBox="0 0 16 10"><path d="M2 2 L8 7 L14 2" fill="none" stroke="#e2323a" stroke-width="2.5"/></svg>
    </div>
  </section>

  <div class="tile tile-guarantee">
    <svg class="trophy" width="50" height="50" viewBox="0 0 50 50">
      <path d="M13 4 H37 V16 C37 26 31 31 25 31 C19 31 13 26 13 16 Z" fill="#fff"/>
      <path d="M13 8 H5 C5 18 10 22 15 22 M37 8 H45 C45 18 40 22 35 22" fill="none" stroke="#fff" stroke-width="3"/>
      <rect x="22" y="30" width="6" height="9" fill="#fff"/>
      <rect x="14" y="39" width="22" height="6" fill="#fff"/>
    </svg>
    <div class="label">NÖJDGARANTI</div>
    <div class="value">100%</div>
  </div>

  <div class="tile tile-order">
    <div class="title">BESTÄLL LOGOTYP</div>
    <svg class="clock" width="90" height="92" viewBox="0 0 90 92">
      <path d="M45 6 A40 40 0 1 1 8 60" fill="none" stroke="#fff" stroke-width="3.5"/>
      <path d="M2 52 L8 62 L15 53" fill="none" stroke="#fff" stroke-width="3"/>
      <text x="45" y="57" text-anchor="middle" fill="#fff" font-family="Nunito Sans, sans-serif" font-size="36">24h</text>
    </svg>
    <div class="price">FRÅN 1495:-</div>
  </div>

  <div class="tile tile-reviews">
    <svg class="stars" width="176" height="32" viewBox="0 0 176 32">
      <g fill="#fff">
        <path id="star" d="M16 1 L20 11.5 L31 12 L22.5 19 L25.5 30 L16 23.8 L6.5 30 L9.5 19 L1 12 L12 11.5 Z"/>
        <use href="#star" x="36"/><use href="#star" x="72"/><use href="#star" x="108"/><use href="#star" x="144"/>
      </g>
    </svg>
    <div class="score">9/10 - Betygsätter UTMÄRKT</div>
    <div class="count">200+ omdömen</div>
    <div class="love">Våra kunder älskar oss!</div>
    <div class="source">
      <svg width="14" height="12" viewBox="0 0 14 12"><path d="M1 6 L5 10 L13 1" fill="none" stroke="#fb9a3a" stroke-width="2.5"/></svg>
      RECENSERA
    </div>
  </div>
</body>
</html>
```